Rolling Nest - Portable Skateboard Display, Organizer, & Stand

Single Webpage for a new company that just launched our first product, the "Rolling Nest Skateboard Stand". This is a consumer product targeted toward parents (especially moms) with kids who have skateboards laying around. Our product is a storage/display/stand that keeps skateboards off of the ground and wheels away from walls. The website design needs to really sell the product as a Portable and Quality product, which can be put anywhere in the home. The website should appeal to adults (Moms especially) and help them quickly understand the versatility, flexibility, high quality, simplicity, and use of the Rolling Nest Skateboard stand. Our website can be viewed at www.rollingnest.example - we'd like to continue to link visitors to our Marketvale product listing for purchases (in the design you submit). Please review the attached creative files and feel free to reach out for additional information.

Target Market(s)

Parents (specifically Moms) with children who own skateboards, interested in keeping a clean and organized home.

Industry/Entity Type

It Company

Number of Pages Required

1 page

Font styles to use
Sans Serif

Requirements
Must have
• Must express the Portability, Quality, and Flexibility of the product. (It can be moved / placed anywhere, does not require mounting or drilling holes)
Nice to have
• Really sell the ease of use and benefit.
Should not have
• Should not be overly complex or cluttered.

```html
<!DOCTYPE html>
<html lang="en">
<head>
<meta charset="utf-8">
<title>Rolling Nest – Skateboard Stand</title>
<link href="https://fonts.googleapis.com/css2?family=Roboto:wght@300;400;500;700;900&display=swap" rel="stylesheet">
<style>
:root{
  --blue:#1f6fc0;
  --blue-dark:#185a9e;
  --ink:#2b2b2b;
  --muted:#8a8a8a;
  --line:#e3e3e3;
  --grey-band:#f0f0f0;
  --footer:#1e1e1e;
  --white:#ffffff;
}
*{box-sizing:border-box;margin:0;padding:0}
html,body{width:682px;height:1200px;overflow:hidden;background:var(--white);font-family:'Roboto',Arial,sans-serif;color:var(--ink)}
.page{width:682px;height:1200px;position:relative;overflow:hidden}

/* header */
.site-header{height:50px;display:flex;align-items:center;justify-content:space-between;padding:0 52px 0 56px}
.brand{display:flex;align-items:center;gap:7px;font-weight:700;font-size:14px;color:var(--blue);line-height:1}
.brand-mark{width:22px;height:22px;background:var(--blue)}
.main-nav{display:flex;align-items:center;gap:22px;font-size:8px;color:var(--muted)}
.main-nav a{color:inherit;text-decoration:none}
.main-nav a.active{color:var(--ink);font-weight:500}
.account-btn{width:20px;height:20px;border-radius:50%;background:#333;display:flex;align-items:center;justify-content:center;margin-left:8px}

/* hero */
.hero{height:320px;position:relative;background:linear-gradient(100deg,#3d4a3c 0%,#8c8170 30%,#d9d2c4 45%,#b59b76 65%,#6b5540 100%)}
.hero-title{position:absolute;right:58px;top:200px;text-align:right;color:var(--white);font-weight:700;font-size:26px;line-height:1.15;text-shadow:0 2px 4px rgba(0,0,0,.4)}
.hero-arrow{position:absolute;top:148px;width:14px;height:22px;background:rgba(0,0,0,.35);display:flex;align-items:center;justify-content:center}
.hero-arrow.prev{left:0}.hero-arrow.next{right:0}

/* shipping + products */
.shipping{padding-top:52px;text-align:center}
.shipping h2{font-size:19px;font-weight:500;color:var(--blue)}
.shipping h2 span{color:var(--ink)}
.product-row{display:flex;justify-content:center;gap:16px;margin-top:24px}
.product-card{width:128px;height:140px;border:1px solid var(--line);text-align:center;padding-top:14px}
.product-shot{width:64px;height:64px;margin:0 auto}
.price{font-size:10px;margin-top:10px;color:var(--ink)}
.market-badge{width:44px;height:9px;margin:6px auto 0;background:#e8e3d6;border-radius:2px}

/* features band */
.features{position:absolute;top:670px;left:0;width:682px;height:350px;background:var(--grey-band);padding:36px 84px 0}
.features .intro{font-size:6.5px;line-height:1.6;color:var(--muted);text-align:center;padding:0 40px}
.feature-list{display:grid;grid-template-columns:1fr 1fr;row-gap:16px;column-gap:20px;margin-top:26px;list-style:none}
.feature-list li{display:flex;align-items:center;gap:6px;font-size:9px;font-weight:500;color:var(--blue-dark)}
.testimonial-row{display:flex;margin-top:28px;height:180px}
.testimonial{width:254px;background:var(--blue);color:var(--white);padding:30px 26px 0 34px;position:relative}
.testimonial .quote-mark{position:absolute;left:18px;top:22px;font-size:22px;font-weight:900;line-height:1}
.testimonial p{font-size:9px;line-height:1.6}
.testimonial cite{display:block;margin-top:14px;font-size:8px;font-style:normal;opacity:.8}
.video{flex:1;position:relative;background:linear-gradient(90deg,#d9d4cc 0%,#b8b0a4 45%,#5a4a3e 70%,#c9c2b6 100%)}
.play{position:absolute;left:50%;top:50%;width:22px;height:22px;margin:-11px 0 0 -11px;border-radius:50%;background:var(--blue);display:flex;align-items:center;justify-content:center}

/* contact */
.contact-bar{position:absolute;top:1040px;left:56px;right:56px;display:flex;align-items:center;gap:18px;font-size:6.5px;color:var(--muted)}
.contact-bar .item{display:flex;align-items:center;gap:4px}
.newsletter{margin-left:auto;display:flex;align-items:center;gap:6px}
.newsletter .field{width:80px;height:14px;border:1px solid var(--line);font-size:6px;padding:3px 4px;color:#bbb}
.newsletter .go{width:14px;height:14px;background:#333}

/* footer */
.site-footer{position:absolute;top:1090px;left:0;width:682px;height:110px;background:var(--footer);text-align:center;padding-top:28px}
.social{display:flex;justify-content:center;gap:8px}
.social span{width:16px;height:16px;background:#3a3f4a}
.social span:first-child{background:var(--blue)}
.footer-nav{margin-top:16px;font-size:6.5px;color:#aaa;display:flex;justify-content:center;gap:10px}
.copyright{margin-top:6px;font-size:6px;color:#777}
</style>
</head>
<body>
<div class="page">

  <header class="site-header">
    <div class="brand"><span class="brand-mark"></span>Rolling Nest</div>
    <nav class="main-nav">
      <a class="active" href="#">Home</a>
      <a href="#">About Product</a>
      <a href="#">Buy Now</a>
      <a href="#">Contact us</a>
      <span class="account-btn">
        <svg width="10" height="10" viewBox="0 0 10 10"><circle cx="5" cy="3.3" r="2" fill="#fff"/><path d="M1.2 9.5c0-2.2 1.7-3.6 3.8-3.6s3.8 1.4 3.8 3.6z" fill="#fff"/></svg>
      </span>
    </nav>
  </header>

  <section class="hero" role="img" aria-label="Skateboard resting upright in a green stand inside a bright home entryway">
    <span class="hero-arrow prev"><svg width="6" height="8" viewBox="0 0 6 8"><path d="M5 0L1 4l4 4" stroke="#fff" fill="none"/></svg></span>
    <span class="hero-arrow next"><svg width="6" height="8" viewBox="0 0 6 8"><path d="M1 0l4 4-4 4" stroke="#fff" fill="none"/></svg></span>
    <h1 class="hero-title">Keep Your Board<br>Where You Want It!</h1>
  </section>

  <section class="shipping">
    <h2>FREE Shipping <span>For Premium Members And Orders</span> Over $35!</h2>
    <div class="product-row">
      <div class="product-card">
        <div class="product-shot" role="img" aria-label="Cream skateboard stand with board" style="background:linear-gradient(160deg,#2c3140 40%,#efe6cf 40%)"></div>
        <div class="price">$19.95</div><div class="market-badge"></div>
      </div>
      <div class="product-card">
        <div class="product-shot" role="img" aria-label="Grey skateboard stand with board" style="background:linear-gradient(160deg,#2c3140 40%,#8f8f8f 40%)"></div>
        <div class="price">$19.95</div><div class="market-badge"></div>
      </div>
      <div class="product-card">
        <div class="product-shot" role="img" aria-label="Red skateboard stand with board" style="background:linear-gradient(160deg,#2c3140 40%,#e23a4e 40%)"></div>
        <div class="price">$19.95</div><div class="market-badge"></div>
      </div>
      <div class="product-card">
        <div class="product-shot" role="img" aria-label="Green skateboard stand with board" style="background:linear-gradient(160deg,#2c3140 40%,#7ed321 40%)"></div>
        <div class="price">$19.95</div><div class="market-badge"></div>
      </div>
    </div>
  </section>

  <section class="features">
    <p class="intro">The Rolling Nest stand gives every skateboard a proper home. It needs no drilling or mounting, so you can set it in the hall, the garage or a bedroom corner and move it whenever you like. Sturdy molded build keeps boards upright and tidy, protects walls from wheel marks and keeps the floor clear, so the whole family can walk through the house without tripping over decks left lying around.</p>
    <ul class="feature-list">
      <li><svg width="9" height="9" viewBox="0 0 9 9"><circle cx="4.5" cy="4.5" r="4.5" fill="#1f6fc0"/><path d="M2.3 4.6l1.5 1.4 3-3" stroke="#fff" stroke-width="1.2" fill="none"/></svg>Keeps Boards Off The Ground - No More Tripping!</li>
      <li><svg width="9" height="9" viewBox="0 0 9 9"><circle cx="4.5" cy="4.5" r="4.5" fill="#1f6fc0"/><path d="M2.3 4.6l1.5 1.4 3-3" stroke="#fff" stroke-width="1.2" fill="none"/></svg>Can Be Used Both Vertically And Horizontally</li>
      <li><svg width="9" height="9" viewBox="0 0 9 9"><circle cx="4.5" cy="4.5" r="4.5" fill="#1f6fc0"/><path d="M2.3 4.6l1.5 1.4 3-3" stroke="#fff" stroke-width="1.2" fill="none"/></svg>Storage Area For Tools And Accessories</li>
      <li><svg width="9" height="9" viewBox="0 0 9 9"><circle cx="4.5" cy="4.5" r="4.5" fill="#1f6fc0"/><path d="M2.3 4.6l1.5 1.4 3-3" stroke="#fff" stroke-width="1.2" fill="none"/></svg>Keeps Wheels Away From Walls - No More Marks!</li>
    </ul>
    <div class="testimonial-row">
      <blockquote class="testimonial">
        <span class="quote-mark">“</span>
        <p>Donec vestibulum odio sem, laoreet massa ullamcorper id. Donec molestie nisi et tellus hac dant vehicula. Nunc eu ligula sed quam pulvinar maximus in vitae eros. Proin porta fermentum ipsum, sit porttitor turpis venenatis.</p>
        <cite>Sam Reed, City Name</cite>
      </blockquote>
      <div class="video" role="img" aria-label="Video still of a skateboard being placed into the stand">
        <span class="play"><svg width="8" height="8" viewBox="0 0 8 8"><path d="M2 1l5 3-5 3z" fill="#fff"/></svg></span>
      </div>
    </div>
  </section>

  <div class="contact-bar">
    <span class="item"><svg width="7" height="9" viewBox="0 0 7 9"><path d="M3.5 9S0 5.2 0 3.4a3.5 3.5 0 017 0C7 5.2 3.5 9 3.5 9z" fill="#999"/><circle cx="3.5" cy="3.4" r="1.2" fill="#fff"/></svg>Suite 12, 48 Harbor Lane, Bayview, CA 90000</span>
    <span class="item"><svg width="8" height="8" viewBox="0 0 8 8"><path d="M1.5 0l1.5 2-1 1c.6 1.3 1.5 2.2 2.8 2.8l1-1L8 6.3 6.6 8C3 7.6.4 5 0 1.4z" fill="#999"/></svg>1-800-555-0142</span>
    <span class="item"><svg width="9" height="7" viewBox="0 0 9 7"><rect width="9" height="7" fill="#999"/><path d="M0 0l4.5 3.8L9 0" stroke="#fff" fill="none"/></svg>hello@rollingnest.example</span>
    <span class="newsletter">Newsletter <span class="field">Email</span><span class="go"></span></span>
  </div>

  <footer class="site-footer">
    <div class="social"><span></span><span></span><span></span><span></span></div>
    <div class="footer-nav"><span>Home</span><span>About Product</span><span>Buy Now</span><span>Contact us</span></div>
    <div class="copyright">Copyright © 2016 · Rolling Nest Co. · All rights reserved.</div>
  </footer>

</div>
</body>
</html>
```